Lotuvan Cafe Menu rev.01

Design an elegant menu for Khmer restaurant in Melbourne.

-Size and format can be proposed (not bigger than A3)
-Food and beverages split (separate sides of the menu)
-Sample excel file - Food attached
-Sample Menu Pdf attached (just to get an idea)
-Details shall be reviewed and considered
-Prices in AUD
-Easy to print and clean (format need to to printable)
-Provision for future updates.

If you have any further question please let us know.
Regards,

Dexter

Target Market(s)

Customers win the restaurant

Industry/Entity Type

Hospitality - Restaurant

Colors

Designer to choose colors to be used in the design.

Requirements
Must have
• Authentic touch - clear structure
Nice to have
• Welcome about the restaurant. Complete information - see sample menu

```html
<!DOCTYPE html>
<html lang="en">
<head>
<meta charset="utf-8">
<title>Lotuvan Cafe Menu</title>
<link rel="stylesheet" href="https://fonts.googleapis.com/css2?family=Roboto+Slab:wght@700;800&family=Cormorant+Garamond:wght@500;600&family=Montserrat:wght@600&display=swap">
<style>
  :root{
    --backdrop:#e7e4df;
    --page:#141312;
    --page-edge:#1d1c1a;
    --gold:#b3a373;
    --gold-soft:#8f8461;
    --pill-ink:#17150f;
    --veg:#6fae3f;
    --vegan:#2f7d3a;
    --gf:#e38b1c;
    --spicy:#c53a2a;
    --peanut:#dfa84c;
  }
  *{box-sizing:border-box;margin:0;padding:0}
  html,body{width:1200px;height:500px;overflow:hidden;background:var(--backdrop)}
  .canvas{position:relative;width:1200px;height:500px}
  .page{
    position:absolute;top:77px;width:246px;height:346px;
    background:radial-gradient(ellipse at 40% 30%,var(--page-edge),var(--page) 70%);
    box-shadow:0 2px 6px rgba(0,0,0,.25);
    color:var(--gold);
  }
  .page::before{
    content:"";position:absolute;inset:10px;border:0.6px solid var(--gold-soft);
  }
  .page--cover{left:52px}
  .page--bites{left:335px}
  .page--khmer{left:619px}
  .page--salads{left:903px}

  .brand{
    position:absolute;left:0;right:0;top:112px;text-align:center;
    font-family:"Roboto Slab",serif;font-weight:800;font-size:30px;
    color:var(--gold);letter-spacing:.5px;line-height:1;
  }

  .section-pill{
    position:absolute;left:26px;height:17px;
    background:var(--gold);color:var(--pill-ink);border-radius:6px;
    font-family:"Roboto Slab",serif;font-weight:800;
    display:flex;align-items:center;padding:0 5px;white-space:nowrap;
  }
  .section-pill--large{font-size:13.5px;letter-spacing:.6px}
  .section-pill--small{font-size:9px;letter-spacing:.7px}

  .item{position:absolute;left:26px;width:182px}
  .item__row{
    display:flex;align-items:baseline;
    font-family:"Cormorant Garamond",serif;font-weight:500;
    font-size:8.4px;letter-spacing:.2px;line-height:1;white-space:nowrap;
  }
  .item__leader{flex:1;border-bottom:0.7px dotted var(--gold);margin:0 2px 1px}
  .item__desc{
    font-family:"Cormorant Garamond",serif;font-weight:500;
    font-size:3.7px;line-height:1.25;margin-top:1px;width:150px;
  }

  .dish{position:absolute;border-radius:50%;box-shadow:0 1px 3px rgba(0,0,0,.6)}
  .dish--fries{background:radial-gradient(ellipse,#a4481f 0 45%,#e9eef2 50% 62%,#3c6fa8 66%)}
  .dish--leaf{background:radial-gradient(circle,#4f6d37 0 40%,#a9c9ad 45%)}
  .dish--rolls{background:radial-gradient(circle,#d79a45 0 38%,#f6f4ee 44%)}
  .dish--tray{border-radius:4px;transform:rotate(10deg);background:linear-gradient(135deg,#6b2c1c,#c98a3c 40%,#e0b25e 55%,#5a2417)}
  .dish--scallop{background:radial-gradient(ellipse,#9c8f5e 0 45%,#f0efe9 52% 64%,#3a5a9a 67%,#eef0f4 72%)}
  .dish--noodle-soup{background:radial-gradient(ellipse,#c9b99a 0 35%,#d86a3c 42%,#e8e2d3 52%,#f7f6f2 60%)}
  .dish--stirfry{background:radial-gradient(circle,#8a5a26 0 45%,#f5f4ef 52%)}
  .dish--soup-bowl{background:radial-gradient(ellipse,#c7a27b 0 45%,#f3f2ee 55%)}
  .dish--rice{background:radial-gradient(ellipse,#d8d2bf 0 55%,#f3f3ef 62%)}
  .dish--glass-noodle{background:radial-gradient(ellipse,#c38b3f 0 35%,#e7e3d4 48%,#3e6e9c 62%,#dfe6ee 70%)}
  .dish--beef{background:radial-gradient(ellipse,#8b3f3a 0 38%,#5b8a3a 48%,#f4f4f2 58%)}
  .dish--tofu{background:radial-gradient(ellipse,#2f3b1e 0 30%,#b77a39 42%,#f3f1ea 58%,#3f7a4b 64%,#f3f1ea 68%)}
  .dish--cover-salad{background:radial-gradient(circle,#b8925f 0 35%,#4d7a39 45%,#f5f5f2 58%)}
  .dish--cover-dessert{background:radial-gradient(circle,#4a2a1e 0 18%,#b33a5e 24%,#f1f0ec 34%)}
  .dish--cover-chicken{background:radial-gradient(circle,#b85a28 0 38%,#7a8f3e 48%,#f4f3ef 58%)}

  .notes{
    position:absolute;left:27px;top:259px;width:190px;list-style:none;
    font-family:"Cormorant Garamond",serif;font-weight:500;font-size:4.1px;line-height:1.85;
  }
  .notes li::before{content:"\2022";margin-right:4px}

  .legend{
    position:absolute;height:9px;border:0.6px solid var(--gold-soft);border-radius:3px;
    display:flex;align-items:center;justify-content:space-around;padding:0 3px;
    font-family:"Montserrat",sans-serif;font-weight:600;font-size:3.6px;letter-spacing:.15px;
  }
  .legend__key{display:flex;align-items:center;gap:2px;white-space:nowrap}
  .legend__badge{
    width:5px;height:5px;border-radius:50%;color:#fff;
    font-size:2.6px;display:flex;align-items:center;justify-content:center;
  }
  .legend__badge--veg{background:var(--veg)}
  .legend__badge--vegan{background:var(--vegan)}
  .legend__badge--gf{background:var(--gf)}
  .legend__icon{width:5px;height:5px}
  .page--cover .legend{left:26px;top:310px;width:192px}
  .page--bites .legend,.page--khmer .legend,.page--salads .legend{left:34px;top:318px;width:185px}
</style>
</head>
<body>
<div class="canvas">

  <!-- Cover -->
  <section class="page page--cover">
    <div class="brand">Lotuvan Cafe</div>
    <div class="dish dish--cover-salad" style="left:26px;top:200px;width:52px;height:51px" role="img" aria-label="Photo of a rice salad on a white plate"></div>
    <div class="dish dish--cover-dessert" style="left:89px;top:220px;width:45px;height:38px" role="img" aria-label="Photo of a plated dessert with an orchid"></div>
    <div class="dish dish--cover-chicken" style="left:146px;top:209px;width:77px;height:62px" role="img" aria-label="Photo of grilled chicken with salad"></div>
    <ul class="notes">
      <li>10% surcharge on public holiday</li>
      <li>All prices are included GST</li>
      <li>All prices are subject to be change without prior notice</li>
      <li>If you are concerned with allergies to certain ingredients please inform our staff.</li>
      <li>Food ingredients and prices are subject to be changed without prior notice</li>
    </ul>
    <div class="legend">
      <span class="legend__key"><span class="legend__badge legend__badge--veg">V</span>Vegetarian</span>
      <span class="legend__key"><span class="legend__badge legend__badge--vegan">VE</span>Vegan</span>
      <span class="legend__key"><span class="legend__badge legend__badge--gf">G</span>Gluten free</span>
      <span class="legend__key"><svg class="legend__icon" viewBox="0 0 10 10"><path d="M4 1 Q6 1 6 3 Q5 8 2 9 Q4 6 4 3Z" fill="#c53a2a"/></svg>Rate of Spicy</span>
      <span class="legend__key"><svg class="legend__icon" viewBox="0 0 10 10"><ellipse cx="3.5" cy="5" rx="3" ry="2.4" fill="#dfa84c"/><ellipse cx="7" cy="5" rx="2.6" ry="2.1" fill="#dfa84c"/></svg>Contain Peanut</span>
    </div>
  </section>

  <!-- Tasty Bites -->
  <section class="page page--bites">
    <div class="section-pill section-pill--large" style="top:21px">TASTY BITES</div>
    <div class="item" style="top:47px">
      <div class="item__row"><span>BETEL LEAF</span><span class="item__leader"></span><span>$4.50</span></div>
      <p class="item__desc">A traditional Cambodian appetizer, betel leafs with Asian Pomegranate, prawns, herbs and special Lotuvan sauce with a dust of peanuts or coconut shredded (1 pcs)</p>
    </div>
    <div class="dish dish--fries" style="left:32px;top:72px;width:62px;height:36px" role="img" aria-label="Photo of crispy sweet potato fries"></div>
    <div class="dish dish--leaf" style="left:164px;top:63px;width:50px;height:48px" role="img" aria-label="Photo of betel leaf bites"></div>
    <div class="item" style="top:115px">
      <div class="item__row"><span>CRISPY SWEET POTATOES</span><span class="item__leader"></span><span>$6.00</span></div>
      <p class="item__desc">Fritted finger strips of sweet potatoes served in a bowl</p>
    </div>
    <div class="item" style="top:134px">
      <div class="item__row"><span>SPRING ROLLS</span><span class="item__leader"></span><span>$10.20</span></div>
      <p class="item__desc">Deep fried roll with pork and prawns, vegetable (3 pcs)</p>
    </div>
    <div class="dish dish--rolls" style="left:47px;top:154px;width:43px;height:42px" role="img" aria-label="Photo of spring rolls with dipping sauce"></div>
    <div class="dish dish--tray" style="left:126px;top:151px;width:83px;height:44px" role="img" aria-label="Photo of spring rolls on a tray"></div>
    <div class="item" style="top:203px">
      <div class="item__row"><span>VEGETARIAN SPRING ROLLS</span><span class="item__leader"></span><span>$9.00</span></div>
      <p class="item__desc">Deep fired roll, vegetable (3 pcs)</p>
    </div>
    <div class="item" style="top:225px">
      <div class="item__row"><span>BBQ SCALLOP</span><span class="item__leader"></span><span>$10.00</span></div>
      <p class="item__desc">Sea scallop with herbs and special Lotuvan dressing (2 pcs)</p>
    </div>
    <div class="dish dish--scallop" style="left:74px;top:245px;width:99px;height:66px" role="img" aria-label="Photo of grilled scallop skewers with lemon"></div>
    <div class="legend">
      <span class="legend__key"><span class="legend__badge legend__badge--veg">V</span>Vegetarian</span>
      <span class="legend__key"><span class="legend__badge legend__badge--vegan">VE</span>Vegan</span>
      <span class="legend__key"><span class="legend__badge legend__badge--gf">G</span>Gluten free</span>
      <span class="legend__key"><svg class="legend__icon" viewBox="0 0 10 10"><path d="M4 1 Q6 1 6 3 Q5 8 2 9 Q4 6 4 3Z" fill="#c53a2a"/></svg>Rate of Spicy</span>
      <span class="legend__key"><svg class="legend__icon" viewBox="0 0 10 10"><ellipse cx="3.5" cy="5" rx="3" ry="2.4" fill="#dfa84c"/><ellipse cx="7" cy="5" rx="2.6" ry="2.1" fill="#dfa84c"/></svg>Contain Peanut</span>
    </div>
  </section>

  <!-- Khmer Breakfast or Lunch -->
  <section class="page page--khmer">
    <div class="section-pill section-pill--small" style="top:22px">KHMER BREAKFAST OR LUNCH</div>
    <div class="item" style="top:45px">
      <div class="item__row"><span>KUY TEAV PHNOM PENH</span><span class="item__leader"></span><span>$15.50</span></div>
      <p class="item__desc">Traditional Cambodian noodle soup, rice and yellow noodles, choice of Pork, Beef or Seafood</p>
    </div>
    <div class="dish dish--noodle-soup" style="left:112px;top:67px;width:100px;height:63px" role="img" aria-label="Photo of noodle soup with prawns"></div>
    <div class="dish dish--stirfry" style="left:46px;top:108px;width:60px;height:48px" role="img" aria-label="Photo of stir-fried noodles"></div>
    <div class="item" style="top:157px">
      <div class="item__row"><span>LOT CHA</span><span class="item__leader"></span><span>$14.50</span></div>
      <p class="item__desc">Rice drop noodles with Chinese chives, bean sprouts, chicken, beef ham and a dust of special Lotuvan sauce</p>
    </div>
    <div class="item" style="top:184px">
      <div class="item__row"><span>KUY TEAV CHAR</span><span class="item__leader"></span><span>$14.80</span></div>
      <p class="item__desc">Stir-fried rice noodles, minced pork, ham, egg, bean sprouts and peanut sauce</p>
    </div>
    <div class="dish dish--soup-bowl" style="left:137px;top:198px;width:57px;height:35px" role="img" aria-label="Photo of a noodle bowl with prawns"></div>
    <div class="item" style="top:237px">
      <div class="item__row"><span>LEMONGRASS FRIED RICE</span><span class="item__leader"></span><span>$16.50</span></div>
      <p class="item__desc">Deep fired roll, vegetable (3 pcs)</p>
    </div>
    <div class="dish dish--rice" style="left:46px;top:255px;width:80px;height:53px" role="img" aria-label="Photo of lemongrass fried rice"></div>
    <div class="legend">
      <span class="legend__key"><span class="legend__badge legend__badge--veg">V</span>Vegetarian</span>
      <span class="legend__key"><span class="legend__badge legend__badge--vegan">VE</span>Vegan</span>
      <span class="legend__key"><span class="legend__badge legend__badge--gf">G</span>Gluten free</span>
      <span class="legend__key"><svg class="legend__icon" viewBox="0 0 10 10"><path d="M4 1 Q6 1 6 3 Q5 8 2 9 Q4 6 4 3Z" fill="#c53a2a"/></svg>Rate of Spicy</span>
      <span class="legend__key"><svg class="legend__icon" viewBox="0 0 10 10"><ellipse cx="3.5" cy="5" rx="3" ry="2.4" fill="#dfa84c"/><ellipse cx="7" cy="5" rx="2.6" ry="2.1" fill="#dfa84c"/></svg>Contain Peanut</span>
    </div>
  </section>

  <!-- Salads -->
  <section class="page page--salads">
    <div class="section-pill section-pill--large" style="top:21px">SALADS</div>
    <div class="item" style="top:45px;width:186px">
      <div class="item__row"><span>GLASS NOODLE SALAD</span><span class="item__leader"></span><span>$20.00</span></div>
      <p class="item__desc">With Chicken or Pork</p>
    </div>
    <div class="dish dish--glass-noodle" style="left:92px;top:58px;width:117px;height:79px" role="img" aria-label="Photo of glass noodle salad in a blue bowl"></div>
    <div class="item" style="top:143px;width:186px">
      <div class="item__row"><span>BEEF SALAD</span><span class="item__leader"></span><span>$22.00</span></div>
      <p class="item__desc">With home made dressing &amp; herbs</p>
    </div>
    <div class="dish dish--beef" style="left:41px;top:163px;width:100px;height:61px" role="img" aria-label="Photo of beef salad with tomatoes and herbs"></div>
    <div class="item" style="top:233px;width:186px">
      <div class="item__row"><span>TOFU SALAD</span><span class="item__leader"></span><span>$19.50</span></div>
      <p class="item__desc">Mixed Asian salad with herbs &amp; coconut dressing</p>
    </div>
    <div class="dish dish--tofu" style="left:76px;top:252px;width:113px;height:58px" role="img" aria-label="Photo of tofu salad with greens"></div>
    <div class="legend">
      <span class="legend__key"><span class="legend__badge legend__badge--veg">V</span>Vegetarian</span>
      <span class="legend__key"><span class="legend__badge legend__badge--vegan">VE</span>Vegan</span>
      <span class="legend__key"><span class="legend__badge legend__badge--gf">G</span>Gluten free</span>
      <span class="legend__key"><svg class="legend__icon" viewBox="0 0 10 10"><path d="M4 1 Q6 1 6 3 Q5 8 2 9 Q4 6 4 3Z" fill="#c53a2a"/></svg>Rate of Spicy</span>
      <span class="legend__key"><svg class="legend__icon" viewBox="0 0 10 10"><ellipse cx="3.5" cy="5" rx="3" ry="2.4" fill="#dfa84c"/><ellipse cx="7" cy="5" rx="2.6" ry="2.1" fill="#dfa84c"/></svg>Contain Peanut</span>
    </div>
  </section>

</div>
</body>
</html>
```